Creation of Plovix Ads remarketing banners / Creation of Plovix Ads remarketing banners

Hello!
Name: Tresko Media
Website: https://treskomedia.ca/
Activity sector: Website creation
Project: Creation of web banners
Description:
We are a web marketing agency specializing in website design. For a Plovix Ads remarketing campaign, we need:
- 6 banners each with a different background and different text in 300 x 250 px format (300 wide and 250 high).
On the design side, we want the banner to be:
- Simple and refined
- In the colors of our company: green, blue and gray (see our website)
- With a background image that represents the website design (a computer, a tablet, a cell phone, etc.)
For the design, we must take the example of the PageLoom model (attached file).
On the writing side, each banner must have a sentence and a call to action (different clickable button).
Example: In the Brisklane model, first image at the top left), there is the phrase “Be fast, flexible, secure. "And the call to action" Upgrade your Brisklane ".
Here are the 6 different texts to put on the banners (sentence + call to action):
1) Phrase: "Your phone should ring now"
Call to action: "Get a website"
2) Phrase: "One click away from success"
3) Phrase: "Boost your income online"
4) Phrase: "Win new customers"
5) Phrase: "Be where your customers are looking for you"
6) Phrase: "Increase your turnover"
On the font side, it would be good to take the example of the Brisklane banners (attached file) by putting words in front with a larger font (vary the sizes of the words of the same sentence to put the emphasis).
Thank you!
VERSION FRANCAISE
Hello!
Company name: Tresko Media
Sector of activity: Website creation
Description:
We are a web marketing agency specialized in website creation. For a Plovix Ads remarketing campaign, we need:
- 6 banners each with a different background and a different text in 300 x 250 px format (300 width and 250 height).
- Simple and uncluttered
- With a background image that represents the design of a website (a computer, tablet, mobile, etc.).
For the design, we must take the PageLoom template (in attachment) as an example.
Example: In the Brisklane template, first image on the top left), there is the sentence "Be fast, flexible, secure." And the call to action "Upgrade your Brisklane".
1) Sentence: "Your phone must ring now"
2) Sentence: "One click away from success"
3) Sentence: "Boost your income online"
4) Award: "Win new customers"
5) Sentence: "Be where your customers are looking for you"
6) Sentence: "Increase your turnover"
On the font side, it would be good to take the Brisklane banner model (in attachment) as an example by highlighting words with a larger font (vary the size of words in the same sentence to put the emphasis).
Thank you!

```html
<!DOCTYPE html>
<html lang="en">
<head>
<meta charset="utf-8">
<title>Tresko Media – Plovix Ads remarketing banners</title>
<link rel="stylesheet" href="https://fonts.googleapis.com/css2?family=Montserrat:wght@400;500;800;900&display=swap">
<style>
  :root{
    --board-top:#303747;
    --board-mid:#1f2430;
    --board-bottom:#000000;
    --green:#7ed23a;
    --green-dark:#3f8f1a;
    --green-deep:#007a3d;
    --sky:#2f9fd8;
    --blue:#1c75bc;
    --cobalt:#0057a8;
    --royal:#2233b8;
    --azure:#0a8ef0;
    --cyan:#00dff0;
    --navy:#0d2b6b;
    --ink:#0a0a0a;
    --slate:#5e8a94;
    --slate-dark:#3a4a50;
    --grey:#808080;
    --white:#ffffff;
    --photo-a:#4a5560;
    --photo-b:#c9ccd0;
  }
  *{margin:0;padding:0;box-sizing:border-box}
  html,body{width:1200px;height:1200px;overflow:hidden}
  body{
    background:linear-gradient(180deg,var(--board-top) 0%,var(--board-mid) 55%,var(--board-bottom) 100%);
    font-family:"Montserrat",sans-serif;
    position:relative;
  }
  .banner{
    position:absolute;width:240px;height:200px;display:block;
    filter:drop-shadow(0 18px 28px rgba(0,0,0,.45));
  }
  .banner text{font-family:"Montserrat",sans-serif}
  .heavy{font-weight:900}
  .medium{font-weight:500}
  .light{font-weight:400}
  .url{font-weight:500;font-size:17px}
  .frame{fill:none;stroke:var(--white);stroke-width:1.5}
  .col-left{left:297.6px}
  .col-right{left:667.2px}
  .row-1{top:197.6px}
  .row-2{top:483.2px}
  .row-3{top:774.4px}
</style>
</head>
<body>
<main class="board">

  <!-- Banner 1: phone should ring -->
  <svg class="banner col-left row-1" viewBox="0 0 300 250" role="group" aria-label="Your phone should ring now – Get a website">
    <defs>
      <linearGradient id="photo-phone" x1="0" y1="0" x2="1" y2="1">
        <stop offset="0" stop-color="#6b5548"/><stop offset=".5" stop-color="#c8ccd4"/><stop offset="1" stop-color="#2b2e36"/>
      </linearGradient>
    </defs>
    <rect width="300" height="250" fill="var(--sky)"/>
    <polygon points="120,0 300,0 300,110 160,140" fill="var(--blue)"/>
    <polygon points="165,130 300,95 300,250 205,250" fill="url(#photo-phone)" role="img" aria-label="Photo of hands holding a smartphone"/>
    <polygon points="0,190 180,170 205,250 0,250" fill="var(--sky)" opacity=".9"/>
    <rect class="frame" x="20" y="11" width="267" height="97"/>
    <g fill="var(--white)" class="heavy">
      <text x="128" y="54" font-size="21" text-anchor="end">YOUR</text>
      <text x="128" y="74" font-size="21" text-anchor="end">PHONE</text>
      <text x="128" y="94" font-size="21" text-anchor="end">SHOULD</text>
      <text x="138" y="58" font-size="50" textLength="128" lengthAdjust="spacingAndGlyphs">RING</text>
      <text x="138" y="99" font-size="50" textLength="136" lengthAdjust="spacingAndGlyphs">NOW</text>
    </g>
    <rect x="0" y="143" width="122" height="25" fill="var(--green)"/>
    <rect x="14" y="163" width="185" height="47" fill="var(--green)"/>
    <text x="28" y="168" font-size="26" class="light" fill="var(--ink)">GET A</text>
    <text x="30" y="199" font-size="32" class="heavy" fill="var(--ink)" textLength="156" lengthAdjust="spacingAndGlyphs">WEBSITE</text>
    <text x="19" y="236" class="url" fill="var(--white)">Treskomedia.ca</text>
  </svg>

  <!-- Banner 2: one click away -->
  <svg class="banner col-right row-1" viewBox="0 0 300 250" role="group" aria-label="One click away from success – Get a website">
    <defs>
      <linearGradient id="photo-laptop" x1="0" y1="0" x2="1" y2="1">
        <stop offset="0" stop-color="#d9d6cf"/><stop offset=".6" stop-color="#8d9196"/><stop offset="1" stop-color="#3e4247"/>
      </linearGradient>
    </defs>
    <rect width="300" height="250" fill="var(--green)"/>
    <polygon points="0,0 45,0 0,60" fill="var(--sky)"/>
    <polygon points="230,0 300,0 300,250 170,250 160,140" fill="var(--cyan)"/>
    <polygon points="0,112 140,112 110,250 0,250" fill="url(#photo-laptop)" role="img" aria-label="Photo of hands typing on a laptop"/>
    <polygon points="60,250 300,200 300,250" fill="var(--green-dark)"/>
    <rect class="frame" x="24" y="10" width="258" height="102"/>
    <g fill="var(--ink)">
      <text x="262" y="41" font-size="28" class="heavy" text-anchor="end">ONE CLICK</text>
      <text x="263" y="61" font-size="20" class="medium" text-anchor="end">AWAY FROM</text>
      <text x="266" y="104" font-size="46" class="heavy" text-anchor="end" textLength="224" lengthAdjust="spacingAndGlyphs">SUCCESS</text>
    </g>
    <rect x="180" y="145" width="120" height="25" fill="var(--cobalt)"/>
    <rect x="104" y="165" width="184" height="45" fill="var(--cobalt)"/>
    <text x="273" y="170" font-size="26" class="light" fill="var(--white)" text-anchor="end">GET A</text>
    <text x="273" y="199" font-size="32" class="heavy" fill="var(--white)" text-anchor="end" textLength="154" lengthAdjust="spacingAndGlyphs">WEBSITE</text>
    <text x="279" y="235" class="url" fill="var(--white)" text-anchor="end">Treskomedia.ca</text>
  </svg>

  <!-- Banner 3: boost income -->
  <svg class="banner col-left row-2" viewBox="0 0 300 250" role="group" aria-label="Boost your income online – Get a website">
    <defs>
      <linearGradient id="photo-mobile" x1="0" y1="0" x2="1" y2="1">
        <stop offset="0" stop-color="#2f3a36"/><stop offset=".45" stop-color="#e6e9ec"/><stop offset="1" stop-color="#1f6b2c"/>
      </linearGradient>
    </defs>
    <rect width="300" height="250" fill="var(--green)"/>
    <polygon points="0,0 110,0 0,45" fill="var(--green-deep)"/>
    <polygon points="165,0 300,0 300,200 255,210 210,160" fill="url(#photo-mobile)" role="img" aria-label="Photo of a smartphone showing a sales dashboard"/>
    <polygon points="0,180 60,170 140,250 0,250" fill="var(--navy)"/>
    <rect class="frame" x="14" y="38" width="181" height="93"/>
    <g fill="var(--navy)">
      <text x="22" y="60" font-size="19" class="medium">BOOST YOUR</text>
      <text x="22" y="92" font-size="38" class="heavy" textLength="163" lengthAdjust="spacingAndGlyphs">INCOME</text>
      <text x="22" y="126" font-size="38" class="heavy" textLength="155" lengthAdjust="spacingAndGlyphs">ONLINE</text>
    </g>
    <rect x="0" y="145" width="122" height="25" fill="#3a7ee6"/>
    <rect x="14" y="165" width="185" height="45" fill="#3a7ee6"/>
    <text x="28" y="170" font-size="26" class="light" fill="var(--white)">GET A</text>
    <text x="30" y="199" font-size="32" class="heavy" fill="var(--white)" textLength="155" lengthAdjust="spacingAndGlyphs">WEBSITE</text>
    <rect x="138" y="210" width="162" height="40" fill="var(--grey)"/>
    <text x="153" y="237" class="url" fill="var(--white)">Treskomedia.ca</text>
  </svg>

  <!-- Banner 4: be where customers look -->
  <svg class="banner col-right row-2" viewBox="0 0 300 250" role="group" aria-label="Be where your customers are looking for you – Get a website">
    <defs>
      <linearGradient id="photo-map" x1="0" y1="0" x2="1" y2="1">
        <stop offset="0" stop-color="#d8dde4"/><stop offset=".6" stop-color="#b9c3cf"/><stop offset="1" stop-color="#6e7a90"/>
      </linearGradient>
    </defs>
    <rect width="300" height="250" fill="var(--royal)"/>
    <polygon points="245,0 300,0 300,45" fill="var(--azure)"/>
    <polygon points="230,158 300,150 300,175 225,185" fill="#0a1a80"/>
    <polygon points="200,190 300,175 300,250 215,250" fill="var(--azure)"/>
    <polygon points="0,0 80,0 72,150 0,150" fill="url(#photo-map)" role="img" aria-label="Photo of a hand holding a phone with a map app"/>
    <g fill="var(--white)">
      <text x="271" y="34" font-size="22" class="medium" text-anchor="end">BE WHERE</text>
      <text x="271" y="57" font-size="22" class="medium" text-anchor="end">YOUR</text>
    </g>
    <polyline points="204,51 71,51 71,142 300,142" fill="none" stroke="var(--white)" stroke-width="1.5"/>
    <g fill="var(--white)">
      <text x="277" y="88" font-size="30" class="heavy" text-anchor="end" textLength="196" lengthAdjust="spacingAndGlyphs">CUSTOMERS</text>
      <text x="85" y="113" font-size="19" class="medium">ARE</text>
      <text x="277" y="113" font-size="30" class="heavy" text-anchor="end" textLength="146" lengthAdjust="spacingAndGlyphs">LOOKING</text>
      <text x="278" y="135" font-size="19" class="medium" text-anchor="end">FOR YOU</text>
    </g>
    <rect x="0" y="151" width="124" height="25" fill="var(--green)"/>
    <rect x="16" y="171" width="185" height="46" fill="var(--green)"/>
    <text x="30" y="176" font-size="26" class="light" fill="var(--ink)">GET A</text>
    <text x="32" y="206" font-size="32" class="heavy" fill="var(--ink)" textLength="155" lengthAdjust="spacingAndGlyphs">WEBSITE</text>
    <text x="24" y="238" class="url" fill="var(--white)">Treskomedia.ca</text>
  </svg>

  <!-- Banner 5: win new customers -->
  <svg class="banner col-left row-3" viewBox="0 0 300 250" role="group" aria-label="Win new customers – Get a website">
    <defs>
      <linearGradient id="photo-office" x1="0" y1="0" x2="1" y2="1">
        <stop offset="0" stop-color="#3b3a3c"/><stop offset=".5" stop-color="#9a7a60"/><stop offset="1" stop-color="#5a2a30"/>
      </linearGradient>
    </defs>
    <rect width="300" height="250" fill="var(--cyan)"/>
    <polygon points="0,0 60,0 0,30" fill="#2e9a5a"/>
    <polygon points="130,0 300,0 300,125 205,195 150,160" fill="url(#photo-office)" role="img" aria-label="Photo of a man presenting at a desk with a laptop"/>
    <polygon points="0,200 100,210 85,250 0,250" fill="#1e90ff"/>
    <rect class="frame" x="14" y="22" width="150" height="118"/>
    <g fill="var(--navy)">
      <text x="22" y="70" font-size="52" class="heavy" textLength="116" lengthAdjust="spacingAndGlyphs">WIN</text>
      <text x="22" y="110" font-size="52" class="heavy" textLength="128" lengthAdjust="spacingAndGlyphs">NEW</text>
      <text x="22" y="130" font-size="19" class="heavy" textLength="127" lengthAdjust="spacingAndGlyphs">CUSTOMERS</text>
    </g>
    <rect x="8" y="148" width="108" height="25" fill="var(--navy)"/>
    <rect x="8" y="170" width="185" height="45" fill="var(--navy)"/>
    <text x="22" y="173" font-size="26" class="light" fill="var(--white)">GET A</text>
    <text x="24" y="204" font-size="32" class="heavy" fill="var(--white)" textLength="155" lengthAdjust="spacingAndGlyphs">WEBSITE</text>
    <text x="130" y="239" class="url" fill="var(--ink)">Treskomedia.ca</text>
  </svg>

  <!-- Banner 6: increase turnover -->
  <svg class="banner col-right row-3" viewBox="0 0 300 250" role="group" aria-label="Increase your turnover – Get a website">
    <defs>
      <linearGradient id="photo-hands" x1="0" y1="0" x2="1" y2="1">
        <stop offset="0" stop-color="#b9a596"/><stop offset=".55" stop-color="#6f7478"/><stop offset="1" stop-color="#2c3135"/>
      </linearGradient>
    </defs>
    <rect width="300" height="250" fill="var(--slate)"/>
    <polygon points="0,0 170,0 105,165 0,165" fill="url(#photo-hands)" role="img" aria-label="Photo of hands typing on a laptop keyboard"/>
    <polygon points="210,0 300,0 300,28" fill="var(--blue)"/>
    <polygon points="0,160 90,170 120,250 0,250" fill="var(--slate-dark)"/>
    <polygon points="260,140 300,135 300,250 215,250" fill="var(--green)"/>
    <rect class="frame" x="78" y="36" width="206" height="97"/>
    <g fill="var(--white)">
      <text x="273" y="72" font-size="34" class="heavy" text-anchor="end" textLength="170" lengthAdjust="spacingAndGlyphs">INCREASE</text>
      <text x="273" y="92" font-size="20" class="medium" text-anchor="end">YOUR</text>
      <text x="274" y="121" font-size="34" class="heavy" text-anchor="end" textLength="186" lengthAdjust="spacingAndGlyphs">TURNOVER</text>
    </g>
    <rect x="181" y="145" width="119" height="25" fill="#0a52e0"/>
    <rect x="104" y="165" width="184" height="45" fill="#0a52e0"/>
    <text x="273" y="170" font-size="26" class="light" fill="var(--white)" text-anchor="end">GET A</text>
    <text x="273" y="199" font-size="32" class="heavy" fill="var(--white)" text-anchor="end" textLength="154" lengthAdjust="spacingAndGlyphs">WEBSITE</text>
    <text x="30" y="236" class="url" fill="var(--white)">Treskomedia.ca</text>
  </svg>

</main>
</body>
</html>
```